Financial Advisor Resource Firm needs business card design

Need business card design for company in Omaha NE called Tallowbrook Partners. We provide resources to financial advisors....workshop programs, retirement analysis, and insurance planning. I would like to see designs that use grays, greens, black, and white colors. The final design should communicate 'collaboration' and be simple yet attractive to financial planning clients. I will attached our logo and another picture of a puzzle piece coming together. I would like the incorporate the puzzle picture somehow, maybe on the back somehow, with color or just the gray scale....OR, the picture be the front of the card with 'Tallowbrook' definition on it (see upload) and then company logo, employee name, title, address on the back (see ppt uploaded). The following disclosure needs to be included somewhere- Advisory services offered through Marlowe Ridge Advisors, LLC.
Updates

I uploaded a svg and ai file of the logo

Target Market(s)

Financial planning clients and financial advisors....so pretty diverse age range of about 40-70.

Industry/Entity Type

Financial Planning

Contact Information for Business Card

Dennis K. Holloway, MBA
Founder/President
5727 E. Larkspur Avenue
Suite 418
Omaha, NE 68297
Phone- (402) 555-0147
Cell- (402) 555-0183
Fax- (402) 555-0129
email- dennis@tallowbrookgroup.example
web address- www.tallowbrookgroup.example

Colors
1b1b1b
474747
d3d3d3
ffffff
9bcb3c
abd036

Requirements
Must have
• Must include logo provided, must be 2 sided, and must have disclosure...all of these items listed in project description

```html
<!DOCTYPE html>
<html lang="en">
<head>
<meta charset="utf-8">
<title>Tallowbrook Partners – Business Card</title>
<link rel="stylesheet" href="https://fonts.googleapis.com/css2?family=Source+Sans+3:wght@400;600;700&family=Montserrat:wght@400&display=swap">
<style>
  :root {
    --backdrop-light: #ececec;
    --backdrop-edge: #cfd0d1;
    --card-dark: #1b1b1b;
    --card-mid: #474747;
    --white: #ffffff;
    --text-light: #e6e6e6;
    --text-muted: #bdbdbd;
    --green: #9bcb3c;
    --rule-gold: #a48b45;
  }
  * { box-sizing: border-box; margin: 0; padding: 0; }
  html, body { width: 800px; height: 1200px; overflow: hidden; }
  body {
    position: relative;
    background: radial-gradient(ellipse at 50% 50%, var(--backdrop-light) 0%, var(--backdrop-edge) 100%);
    font-family: "Source Sans 3", "Myriad Pro", sans-serif;
  }
  .card {
    position: absolute;
    left: 148px;
    width: 504px;
    height: 288px;
    overflow: hidden;
    color: var(--text-light);
    box-shadow: 0 2px 6px rgba(0,0,0,0.25);
  }
  .card--front { top: 170px; border-radius: 11px; }
  .card--back { top: 703px; left: 134px; }
  .card__photo {
    position: absolute; inset: 0;
    background:
      radial-gradient(ellipse at 62% 58%, #4a4a4a 0%, rgba(74,74,74,0) 45%),
      radial-gradient(ellipse at 18% 30%, #3e3e3e 0%, rgba(62,62,62,0) 40%),
      linear-gradient(180deg, #333 0%, var(--card-dark) 100%);
  }
  .brand-name {
    position: absolute;
    color: var(--white);
    font-weight: 600;
    font-size: 31px;
    letter-spacing: 0.5px;
    white-space: nowrap;
  }
  .card--front .brand-name { left: 38px; top: 58px; }
  .card--back .brand-name { left: 0; right: 0; top: 112px; text-align: center; }
  .contact__name {
    position: absolute; left: 30px; top: 149px;
    color: var(--green); font-weight: 700; font-size: 20px;
  }
  .contact__title {
    position: absolute; left: 30px; top: 174px;
    font-size: 13.5px;
  }
  .contact__row {
    position: absolute; left: 30px;
    display: flex; gap: 12px; font-size: 12.5px; white-space: nowrap;
  }
  .contact__row--phones { top: 195px; }
  .contact__row--web { top: 222px; gap: 22px; }
  .contact__item { display: flex; align-items: center; gap: 5px; }
  .contact__item svg { width: 9px; height: 9px; fill: var(--green); }
  .contact__rule {
    position: absolute; left: 30px; top: 243px;
    width: 372px; height: 1px; background: var(--rule-gold);
  }
  .contact__address {
    position: absolute; left: 30px; top: 248px;
    font-size: 13px;
  }
  .tagline {
    position: absolute; left: 0; right: 0; top: 196px;
    text-align: center;
    font-family: "Montserrat", sans-serif;
    font-size: 12.8px; color: var(--text-light);
  }
  .disclosure {
    position: absolute; left: 0; right: 0; bottom: 16px;
    text-align: center;
    font-size: 10px; color: var(--text-muted);
    letter-spacing: 0.2px;
  }
</style>
</head>
<body>

  <section class="card card--front">
    <div class="card__photo" role="img" aria-label="Grayscale photo of business hands joining two puzzle pieces over a desk"></div>
    <div class="brand-name">Tallowbrook Partners</div>
    <div class="contact__name">Dennis K. Holloway, MBA</div>
    <div class="contact__title">Founder/President</div>
    <div class="contact__row contact__row--phones">
      <span class="contact__item">
        <svg viewBox="0 0 10 10"><path d="M2 0.5l2 2-1 1.2c.6 1.3 1.6 2.3 2.9 2.9l1.2-1 2 2-1.4 1.9C4.5 9.5.5 5.5 0.1 1.9z"/></svg>(402) 555-0147</span>
      <span class="contact__item">
        <svg viewBox="0 0 10 10"><path d="M2.5 0h5v10h-5zM3.3 1v7h3.4V1z"/></svg>(402) 555-0183</span>
      <span class="contact__item">
        <svg viewBox="0 0 10 10"><path d="M2.5 0h5v3h2v6h-9V3h2zM3.3 1v2h3.4V1zM2 5v1h6V5z"/></svg>(402) 555-0129</span>
    </div>
    <div class="contact__row contact__row--web">
      <span class="contact__item">
        <svg viewBox="0 0 10 10"><path d="M0 2h10v6H0zM0.6 2.6L5 5.8l4.4-3.2z"/></svg>dennis@tallowbrookgroup.example</span>
      <span class="contact__item">
        <svg viewBox="0 0 10 10"><circle cx="5" cy="5" r="4.6"/><path d="M0.5 5h9M5 0.5v9" stroke="#1b1b1b" stroke-width="0.8"/></svg>www.tallowbrookgroup.example</span>
    </div>
    <div class="contact__rule"></div>
    <div class="contact__address">5727 E. Larkspur Avenue Suite 418 Omaha, NE 68297</div>
  </section>

  <section class="card card--back">
    <div class="card__photo" role="img" aria-label="Grayscale photo of hands fitting puzzle pieces together"></div>
    <div class="brand-name">Tallowbrook Partners</div>
    <p class="tagline">TO COME TOGETHER AND UNITE IN COMMON INTEREST AND FOCUS</p>
    <p class="disclosure">Advisory services offered through Marlowe Ridge Advisors, LLC.</p>
  </section>

</body>
</html>
```